Business Card Design for a Personal Trainer

I need a business card design for my job as a personal trainer. It should have a unique, modern and exclusive design. On the front there should be only my logo with my name and my job. 0163/2918374 Tobias Kellinger Lindenfeldweg 14 80412 Munich Germany The most important contact information is the web adress. it can be bigger than the rest, but its not necessary. The card should be 8,5cmx5,5cm big. Font: Roboto. Colors: black, white, gray, 56c1ff.

```html
<!DOCTYPE html>
<html lang="de">
<head>
<meta charset="utf-8">
<title>Tobias Kellinger – Personal Trainer Visitenkarte</title>
<link rel="stylesheet" href="https://fonts.googleapis.com/css2?family=Roboto:wght@400;500&family=Tinos&display=swap">
<style>
  :root {
    --page-bg: #e9e9e7;
    --card-front: #c3c6c5;
    --card-back: #d3d6d5;
    --ink-white: #ffffff;
    --ink-gray: #8a8d8e;
    --ink-dark: #1d1d1d;
    --corner: #7d8081;
    --band: #b9bcbc;
    --photo-top: #9a9c9d;
    --photo-bottom: #3a3b3c;
  }
  * { margin: 0; padding: 0; box-sizing: border-box; }
  html, body { width: 1200px; height: 892px; overflow: hidden; background: var(--page-bg); }
  .stage {
    position: relative; width: 1200px; height: 892px;
    display: flex; align-items: center; justify-content: center; gap: 60px;
  }
  .card {
    position: relative; width: 520px; height: 336px; overflow: hidden;
    box-shadow: 0 8px 24px rgba(0,0,0,.18);
  }
  /* Front */
  .card--front { background: var(--card-front); display: flex; align-items: center; justify-content: center; }
  .brand { text-align: center; color: var(--ink-white); font-family: "Roboto", sans-serif; }
  .brand__name { font-size: 30px; font-weight: 400; letter-spacing: 2px; line-height: 1; }
  .brand__job {
    display: flex; align-items: center; gap: 10px; justify-content: center;
    margin-top: 6px; font-size: 12px; letter-spacing: 5px; font-weight: 400;
  }
  .brand__job::before, .brand__job::after { content: ""; flex: 1; height: 1px; background: currentColor; }
  /* Back */
  .card--back { background: var(--card-back); }
  .back-brand { position: absolute; top: 38px; left: 170px; color: var(--ink-gray); }
  .back-brand .brand__name { font-size: 22px; }
  .back-brand .brand__job { font-size: 9px; letter-spacing: 4px; margin-top: 4px; }
  .corner { position: absolute; left: 0; width: 22px; height: 22px; background: var(--corner); }
  .corner--top { top: 0; clip-path: polygon(0 0, 100% 0, 0 100%); }
  .corner--bottom { bottom: 0; clip-path: polygon(0 0, 100% 100%, 0 100%); }
  .contact {
    position: absolute; left: 44px; top: 112px;
    border-left: 2px solid var(--ink-dark); padding-left: 12px;
    font-family: "Tinos", serif; font-size: 15px; line-height: 19px; color: var(--ink-dark);
    list-style: none;
  }
  .contact__web { font-size: 16px; }
  .band { position: absolute; left: 160px; right: 0; top: 232px; height: 26px; background: var(--band); }
  .portrait {
    position: absolute; right: 40px; bottom: 0; width: 170px; height: 190px;
    background: linear-gradient(180deg, var(--photo-top), var(--photo-bottom));
  }
</style>
</head>
<body>
<main class="stage">
  <section class="card card--front" aria-label="Vorderseite">
    <div class="brand">
      <p class="brand__name">TOBIAS KELLINGER</p>
      <p class="brand__job">PERSONAL TRAINER</p>
    </div>
  </section>

  <section class="card card--back" aria-label="Rückseite">
    <span class="corner corner--top"></span>
    <span class="corner corner--bottom"></span>
    <div class="brand back-brand">
      <p class="brand__name">TOBIAS KELLINGER</p>
      <p class="brand__job">PERSONAL TRAINER</p>
    </div>
    <ul class="contact">
      <li class="contact__web">www.tobiaskellinger.de</li>
      <li>t.kellinger@mailpost.de</li>
      <li>0163/2918374</li>
      <li>Tobias Kellinger</li>
      <li>Lindenfeldweg 14</li>
      <li>80412 München</li>
    </ul>
    <div class="band"></div>
    <div class="portrait" role="img" aria-label="Schwarz-weiß Foto des Trainers mit verschränkten Armen"></div>
  </section>
</main>
</body>
</html>
```